Make the invisible visible.... and attractive

I have an online course at http://www.brightpathlessons.example/Begin-today.html. I need an attractive graphic to sell the product. The course is a series of video, audio and handout materials set out in 32 lessons and has a free one year confidence course as a bonus.

Target Market(s)

Individuals who have problems with fear or anxiety.

Industry/Entity Type

Audio

```html
<!DOCTYPE html>
<html lang="en">
<head>
<meta charset="utf-8">
<title>Bright Path Course Online – Banner</title>
<link rel="stylesheet" href="https://fonts.googleapis.com/css2?family=Arimo:wght@400;700&family=Roboto+Condensed:wght@700&display=swap">
<style>
  :root {
    --page: #ffffff;
    --sky-top: #173a6e;
    --sky-mid: #2a5c9c;
    --sky-low: #5d93cf;
    --horizon: #b9d8f3;
    --navy: #0b2f5f;
    --badge: #0f3566;
    --badge-ring: #1c73d6;
    --button-top: #3aa2f7;
    --button-bottom: #0b7be0;
    --text: #ffffff;
    --text-soft: #e8f0fa;
  }
  * { margin: 0; padding: 0; box-sizing: border-box; }
  html, body {
    width: 1200px;
    height: 1000px;
    overflow: hidden;
    background: var(--page);
  }
  .banner {
    position: absolute;
    left: 62px;
    top: 77px;
    width: 1079px;
    height: 540px;
    overflow: hidden;
    background:
      radial-gradient(ellipse 70% 30% at 45% 88%, var(--horizon) 0%, rgba(185,216,243,0) 70%),
      linear-gradient(180deg, var(--sky-top) 0%, var(--sky-mid) 50%, var(--sky-low) 85%, var(--sky-mid) 100%);
    font-family: "Arimo", Arial, sans-serif;
    color: var(--text);
  }
  .banner__photo {
    position: absolute;
    left: 0;
    top: 0;
    width: 520px;
    height: 494px;
    background:
      radial-gradient(ellipse 60% 70% at 40% 45%, rgba(170,200,235,0.55) 0%, rgba(90,130,190,0.35) 45%, rgba(40,80,140,0) 80%);
  }
  .brand {
    position: absolute;
    right: 56px;
    top: 34px;
    display: flex;
    align-items: center;
    gap: 14px;
  }
  .brand__tagline {
    font-size: 14px;
    line-height: 20px;
    text-align: right;
    color: var(--text-soft);
  }
  .brand__name {
    font-family: "Arimo", Arial, sans-serif;
    font-weight: 700;
    font-size: 20px;
    color: var(--text);
  }
  .brand__dot {
    width: 22px;
    height: 22px;
    border-radius: 50%;
    background: var(--text);
  }
  .headline {
    position: absolute;
    right: 60px;
    top: 136px;
    font-family: "Roboto Condensed", "Arial Narrow", sans-serif;
    font-weight: 700;
    font-size: 36px;
    line-height: 48px;
    text-align: right;
    color: var(--text);
  }
  .intro {
    position: absolute;
    right: 60px;
    top: 243px;
    font-size: 20px;
    line-height: 28.5px;
    text-align: right;
    color: var(--text);
  }
  .join-button {
    position: absolute;
    left: 811px;
    top: 382px;
    width: 212px;
    height: 46px;
    border-radius: 4px;
    background: linear-gradient(180deg, var(--button-top), var(--button-bottom));
    box-shadow: 3px 4px 6px rgba(0,20,50,0.45);
    color: var(--text);
    font-size: 23px;
    line-height: 46px;
    text-align: center;
    text-decoration: none;
  }
  .footer-band {
    position: absolute;
    left: 0;
    bottom: 0;
    width: 100%;
    height: 46px;
    background: var(--navy);
  }
  .footer-band__text {
    position: absolute;
    right: 60px;
    top: 11px;
    font-size: 19px;
    color: var(--text);
  }
  .bonus-badge {
    position: absolute;
    left: 22px;
    top: 337px;
    width: 184px;
    height: 184px;
    border-radius: 50%;
    background: var(--badge);
    border: 5px solid var(--badge-ring);
    box-shadow: 2px 3px 6px rgba(0,0,0,0.35);
  }
  .bonus-badge__text {
    position: absolute;
    left: 0;
    top: 28px;
    width: 100%;
    text-align: center;
    transform: rotate(-24deg);
    color: var(--text);
  }
  .bonus-badge__lead {
    display: block;
    font-size: 24px;
    line-height: 24px;
  }
  .bonus-badge__detail {
    display: block;
    font-family: "Arimo", Arial, sans-serif;
    font-weight: 700;
    font-size: 19px;
    line-height: 21px;
    margin-top: 2px;
  }
</style>
</head>
<body>
  <section class="banner">
    <div class="banner__photo" role="img" aria-label="Photo of a calm young man wearing headphones, eyes closed, blended into a blue sky"></div>

    <div class="brand">
      <p class="brand__tagline">From arghhh to<br>ahhhhh in one day</p>
      <span class="brand__dot"></span>
      <span class="brand__name">Bright Path</span>
    </div>

    <h1 class="headline">Develop powerful emotional resilience<br>quickly and easily.</h1>

    <p class="intro">
      The Bright Path Course Online gives you everything you need<br>
      to be calm and composed in any situation.<br>
      You will learn the secrets that we teach the emergency<br>
      services and disaster managers around the world.
    </p>

    <a class="join-button" href="http://www.brightpathlessons.example/Begin-today.html">Join Now</a>

    <div class="footer-band">
      <p class="footer-band__text">The course is a series of video, audio and handout materials set out in 32 lessons.</p>
    </div>

    <div class="bonus-badge">
      <p class="bonus-badge__text">
        <span class="bonus-badge__lead">FREE<br>BONUS</span>
        <span class="bonus-badge__detail">one year<br>confidence<br>course</span>
      </p>
    </div>
  </section>
</body>
</html>
```